Business Card Design REAL ESTATE SALES PLEASE DESIGN MY CARD 2COLOR CARD WITH RED AS THE DOMINANT

MOOR PINE REALTY
TorVHA Lic# 04827316
WALTER " WALT " KOVIC Tel 555 555-0142
TorVHA Lic# 00762408 Fax 555 555-0187
Email: walt@waltkovic.example Cell 510 555-0163
48610 FERNHILL COURT HARLOW VALE, ZN 94999

Business

WALTER " WALT " KOVIC
TEL: 555 555-0142 FAX 555 555-0187
Address: 48610 Fernhill Court Union City , CA
EMAIL ADDRESS: walt@waltkovic.example

```html
<!DOCTYPE html>
<html lang="en">
<head>
<meta charset="utf-8">
<title>Moor Pine Realty — Business Card</title>
<link rel="stylesheet" href="https://fonts.googleapis.com/css2?family=Bebas+Neue&family=Mulish:wght@400&display=swap">
<style>
  :root {
    --card-red: #cc1f25;
    --ink-white: #ffffff;
  }
  html, body {
    margin: 0;
    padding: 0;
    width: 1200px;
    height: 702px;
    overflow: hidden;
    background: var(--card-red);
  }
  .business-card {
    position: relative;
    width: 1200px;
    height: 702px;
    background: var(--card-red);
    color: var(--ink-white);
    overflow: hidden;
  }
  .brand-name {
    position: absolute;
    top: 44px;
    right: 59px;
    margin: 0;
    font-family: "Bebas Neue", "Arial Narrow", sans-serif;
    font-weight: 400;
    font-size: 110px;
    line-height: 1;
    letter-spacing: 0.5px;
    white-space: nowrap;
  }
  .agent-name {
    position: absolute;
    left: 62px;
    top: 346px;
    margin: 0;
    font-family: "Bebas Neue", "Arial Narrow", sans-serif;
    font-weight: 400;
    font-size: 80px;
    line-height: 1;
    letter-spacing: 0.5px;
    white-space: nowrap;
  }
  .office-address {
    position: absolute;
    left: 61px;
    top: 444px;
    margin: 0;
    font-family: "Mulish", "Avenir", sans-serif;
    font-size: 42px;
    line-height: 1.2;
    font-style: normal;
    white-space: nowrap;
  }
  .contact-list {
    position: absolute;
    left: 61px;
    top: 558px;
    margin: 0;
    display: grid;
    grid-template-columns: 329px 300px auto;
    font-family: "Mulish", "Avenir", sans-serif;
  }
  .contact-item {
    margin: 0;
  }
  .contact-label {
    margin: 0;
    font-size: 28px;
    line-height: 1.2;
    letter-spacing: 0.5px;
  }
  .contact-value {
    margin: 6px 0 0;
    font-size: 40px;
    line-height: 1.2;
    letter-spacing: -0.3px;
    white-space: nowrap;
  }
</style>
</head>
<body>
  <main class="business-card">
    <h1 class="brand-name">MOOR PINE REALTY</h1>
    <h2 class="agent-name">WALTER "WALT" KOVIC</h2>
    <address class="office-address">48610 Fernhill Court Harlow Vale, ZN 94999</address>
    <dl class="contact-list">
      <div class="contact-item">
        <dt class="contact-label">PHONE</dt>
        <dd class="contact-value">555 555-0142</dd>
      </div>
      <div class="contact-item">
        <dt class="contact-label">FAX</dt>
        <dd class="contact-value">555 555-0187</dd>
      </div>
      <div class="contact-item">
        <dt class="contact-label">EMAIL</dt>
        <dd class="contact-value">walt@waltkovic.example</dd>
      </div>
    </dl>
  </main>
</body>
</html>
```